Data Collection Workbook

We are creating a data gathering booklet that will be completed by our clients (ages 40-90). Due to the volume of information being collected, we are looking for a format that is both inviting to complete and aesthetically pleasing to the eye. The final product will be approximately 20-30 pages, divided into 13 sections. A table of contents, as well as two sample pages are attached.

```html
<!DOCTYPE html>
<html lang="en">
<head>
<meta charset="utf-8">
<title>Content – Data Collection Workbook</title>
<link rel="stylesheet" href="https://fonts.googleapis.com/css2?family=Open+Sans:wght@300;400&display=swap">
<style>
  :root {
    --teal: #3bb3c3;
    --paper: #ffffff;
    --ink: #3a3a3a;
    --rule: #6d6d6d;
    --edge: #5a5a5a;
  }
  * { margin: 0; padding: 0; box-sizing: border-box; }
  html, body {
    width: 848px;
    height: 1200px;
    overflow: hidden;
    background: var(--paper);
  }
  .page {
    position: relative;
    width: 848px;
    height: 1200px;
    background: var(--paper);
    border-left: 2px solid var(--edge);
    font-family: "Open Sans", "Segoe UI", sans-serif;
    color: var(--ink);
    overflow: hidden;
  }
  .header-band {
    position: absolute;
    left: 0; top: 0;
    width: 100%;
    height: 349px;
    background: var(--teal);
  }
  .page-title {
    position: absolute;
    right: 84px;
    top: 228px;
    font-weight: 300;
    font-size: 88px;
    line-height: 1;
    letter-spacing: 1px;
    color: var(--paper);
  }
  .footer-band {
    position: absolute;
    left: 0; bottom: 0;
    width: 100%;
    height: 61px;
    background: var(--teal);
  }
  .toc-rule {
    position: absolute;
    left: 0; top: 0;
    width: 848px;
    height: 1200px;
    pointer-events: none;
  }
  .toc {
    position: absolute;
    left: 108px;
    top: 363px;
    width: 630px;
    list-style: none;
  }
  .toc-item {
    position: relative;
    height: 43.2px;
    font-size: 15.5px;
    line-height: 24px;
    font-weight: 400;
  }
  .toc-page {
    position: absolute;
    left: 563px;
    top: 0;
  }
</style>
</head>
<body>
  <main class="page">
    <div class="header-band"></div>
    <h1 class="page-title">CONTENT</h1>

    <svg class="toc-rule" viewBox="0 0 848 1200" aria-hidden="true">
      <g stroke="var(--rule)" stroke-width="1.5">
        <line x1="658" y1="353" x2="658" y2="1002"/>
        <line x1="648" y1="375" x2="668" y2="375"/>
        <line x1="648" y1="418" x2="668" y2="418"/>
        <line x1="648" y1="461" x2="668" y2="461"/>
        <line x1="648" y1="505" x2="668" y2="505"/>
        <line x1="648" y1="548" x2="668" y2="548"/>
        <line x1="648" y1="591" x2="668" y2="591"/>
        <line x1="648" y1="634" x2="668" y2="634"/>
        <line x1="648" y1="677" x2="668" y2="677"/>
        <line x1="648" y1="720" x2="668" y2="720"/>
        <line x1="648" y1="764" x2="668" y2="764"/>
        <line x1="648" y1="807" x2="668" y2="807"/>
        <line x1="648" y1="850" x2="668" y2="850"/>
      </g>
    </svg>

    <ol class="toc">
      <li class="toc-item">My General Information<span class="toc-page">03</span></li>
      <li class="toc-item">My Spouse's General Information; Family Pets<span class="toc-page">04</span></li>
      <li class="toc-item">Personal Identification Numbers &amp; Access Codes<span class="toc-page">05</span></li>
      <li class="toc-item">Doctors &amp; Professional Advisors<span class="toc-page">07</span></li>
      <li class="toc-item">Financial 0bligations<span class="toc-page">09</span></li>
      <li class="toc-item">Subscriptions &amp; Social Media<span class="toc-page">11</span></li>
      <li class="toc-item">Health Insurance Coverage &amp; Health Inf0rmati0n<span class="toc-page">13</span></li>
      <li class="toc-item">Insurance Coverage<span class="toc-page">15</span></li>
      <li class="toc-item">Important Documents &amp; Other Information<span class="toc-page">17</span></li>
      <li class="toc-item">Assets<span class="toc-page">19</span></li>
      <li class="toc-item">Source of Income/Retirement Benefits<span class="toc-page">21</span></li>
      <li class="toc-item">Monthly Budget in the Event of Incapacity<span class="toc-page">23</span></li>
    </ol>

    <div class="footer-band"></div>
  </main>
</body>
</html>
```